Banner Ad for website hompage - Design Project

We need 4 banner ads for the homepage of a Rent a Car company based in dubai. We rent a wide range of cars but mainly deal in the affordable cars category. Our website colors are mainly red, white and black and I can send pictures of the website (attached) if you want something to compare possible design ideas with. The banners need to promote different messages and must be appealing to the end user. It must also use pictures of cars that exist in our fleet (Pls note: this is only if you are using cars in the banner ad)

The 4 banner ads needed are as follows:
1) should promote something along the lines of we have 20+ models available and reserve a car now (This banner should also have a reserve now button, not the actual button but it's design. The button will be made and coded by us)
2) should promote something along the lines of we offer personalised service and we look after each and every custoemr individually
3) we provide attractive rates based on daily, weekly, monthly and longer rental periods (should also incorporate a reserve now message)
4) Like us on quorvia and follow us on social media for additional offers and discounts (would like for this to have a like button design implemented in it which will be linked to quorvia.)

Also please not the picture file size is 940pixels by 400pixels

Finally: I also need the psd files for the banners.

```html
<!DOCTYPE html>
<html lang="en">
<head>
<meta charset="utf-8">
<title>Special Offer Banner</title>
<link rel="stylesheet" href="https://fonts.googleapis.com/css2?family=Oswald:wght@500;700&family=Passion+One:wght@700&display=swap">
<style>
  :root {
    --ink: #050505;
    --red: #e0120f;
    --red-deep: #a50a08;
    --white: #ffffff;
    --paper: #f3f3f3;
    --bar-top: #5a5a5a;
    --bar-bottom: #2a2a2a;
    --social-blue: #2f5fae;
    --badge-text: #2a3f66;
    --car-light: #f2f2f2;
    --car-mid: #cfcfcf;
    --car-dark: #8a8a8a;
  }
  html, body {
    margin: 0;
    padding: 0;
    overflow: hidden;
    background: var(--ink);
  }
  .banner {
    position: relative;
    width: 1200px;
    height: 511px;
    overflow: hidden;
    background: radial-gradient(ellipse 60% 70% at 55% 35%, #2a2a2a 0%, #111 55%, var(--ink) 100%);
    font-family: "Oswald", "Arial Narrow", sans-serif;
  }
  .swoosh {
    position: absolute;
    left: 0;
    top: 0;
    width: 1200px;
    height: 511px;
  }
  .headline,
  .headline-reflection {
    position: absolute;
    left: 577px;
    margin: 0;
    font-weight: 700;
    font-size: 31px;
    letter-spacing: 0.3px;
    color: var(--red);
    white-space: nowrap;
    line-height: 1;
  }
  .headline { top: 90px; }
  .headline-reflection {
    top: 125px;
    transform: scaleY(-1);
    opacity: 0.18;
    -webkit-mask-image: linear-gradient(to top, #000 0%, transparent 60%);
    mask-image: linear-gradient(to top, #000 0%, transparent 60%);
  }
  .offer-card {
    position: absolute;
    left: 240px;
    top: 112px;
    width: 250px;
    height: 262px;
    background: var(--paper);
    outline: 6px dotted var(--paper);
    outline-offset: 2px;
    transform: rotate(-7deg);
    box-shadow: 0 6px 18px rgba(0,0,0,0.6);
  }
  .offer-title {
    position: absolute;
    left: 18px;
    top: 24px;
    margin: 0;
    font-family: "Passion One", "Arial Black", sans-serif;
    font-weight: 700;
    font-size: 58px;
    line-height: 0.85;
    color: var(--red);
    transform: rotate(-8deg) skewX(-10deg);
    text-shadow: 1px 1px 0 var(--red-deep), 2px 2px 0 var(--red-deep), 3px 3px 0 var(--red-deep), 5px 6px 6px rgba(0,0,0,0.35);
  }
  .offer-title .line-two { display: block; padding-left: 46px; }
  .reserve-button {
    position: absolute;
    left: 20px;
    top: 178px;
    width: 210px;
    height: 62px;
    border-radius: 8px;
    background: linear-gradient(#e8231c, #b80c09);
    box-shadow: inset 0 1px 0 rgba(255,255,255,0.35), 0 3px 6px rgba(0,0,0,0.35);
    color: var(--white);
    font-weight: 700;
    font-size: 26px;
    line-height: 62px;
    text-align: center;
    letter-spacing: 0.3px;
  }
  .car-glow {
    position: absolute;
    left: 510px;
    top: 335px;
    width: 470px;
    height: 80px;
    background: radial-gradient(ellipse at 45% 50%, rgba(230,20,15,0.95) 0%, rgba(180,10,8,0.6) 40%, transparent 72%);
  }
  .car-photo {
    position: absolute;
    left: 512px;
    top: 182px;
    width: 462px;
    height: 190px;
    border-radius: 28px;
    background: linear-gradient(160deg, var(--car-light) 0%, var(--car-mid) 55%, var(--car-dark) 100%);
  }
  .social-bar {
    position: absolute;
    left: 0;
    top: 443px;
    width: 1200px;
    height: 60px;
    background: linear-gradient(var(--bar-top), var(--bar-bottom));
    border-top: 1px solid #777;
    border-bottom: 2px solid #111;
    display: flex;
    align-items: center;
  }
  .social-badge {
    width: 176px;
    height: 52px;
    margin-left: 3px;
    background: var(--white);
    display: flex;
    align-items: center;
    gap: 12px;
    box-sizing: border-box;
  }
  .social-badge .mark {
    width: 52px;
    height: 52px;
    background: var(--social-blue);
  }
  .social-badge .name {
    font-weight: 500;
    font-size: 26px;
    color: var(--badge-text);
  }
  .social-message {
    margin: 0 0 0 24px;
    font-weight: 500;
    font-size: 24px;
    color: var(--white);
    white-space: nowrap;
    letter-spacing: 0.5px;
  }
</style>
</head>
<body>
  <main class="banner">
    <svg class="swoosh" viewBox="0 0 1200 511" aria-hidden="true">
      <path d="M0 420 C 140 330, 330 300, 520 330" fill="none" stroke="rgba(255,255,255,0.10)" stroke-width="10"/>
      <path d="M0 450 C 160 360, 340 330, 560 350" fill="none" stroke="rgba(255,255,255,0.06)" stroke-width="6"/>
      <path d="M640 0 C 820 80, 1040 90, 1200 40" fill="none" stroke="rgba(255,255,255,0.03)" stroke-width="18"/>
    </svg>

    <h1 class="headline">"EXPERIENCE A NEW WORLD ON WHEELS"</h1>
    <p class="headline-reflection" aria-hidden="true">"EXPERIENCE A NEW WORLD ON WHEELS"</p>

    <section class="offer-card">
      <h2 class="offer-title">Special<span class="line-two">offer</span></h2>
      <div class="reserve-button">RESERVE NOW</div>
    </section>

    <div class="car-glow" aria-hidden="true"></div>
    <div class="car-photo" role="img" aria-label="White four-door sedan from the rental fleet, front three-quarter view"></div>

    <footer class="social-bar">
      <div class="social-badge">
        <span class="mark" aria-hidden="true"></span>
        <span class="name">quorvia</span>
      </div>
      <p class="social-message">LIKE US ON QUORVIA AND FOLLOW US ON SOCIAL MEDIA FOR ADDITIONAL OFFERS AND DISCOUNTS</p>
    </footer>
  </main>
</body>
</html>
```